Lumen Grove Business Card & Corporate Pack

Hi my Brand is Lumen Grove. It's a reiki Studio that offers Reiki Healing Services along with other therapies focussed on healing a customers mind & body, spiritually. I need to get a Business Card done mainly and along with other corporate literature (such as letter heads and other related items) at the same time.

My Theme color is a magical Purple. But its in RGB format. So I need to ensure the print comes out with perfect colors since most prints happen in CMYK.

I need the business card to be the main offering and all the others as value additions.

The business card needs to give out a magical, serene, blissful feeling. I prefer very light colors and needs to be inline with the theme color and most importantly practical in printing terms.

The card needs a double sided card design. ILLUSTRATOR DESIGNS ONLY. All Original design files with fonts used and editable fonts should be submitted

MUST INCLUDE

- the logo (LUMEN GROVE)
- Address : No 8, Perera Crescent, Galvin Lane, Colombo 5, Sri Lanka
- Name : Mala Wickramaratne
- Designation : Founder / Reiki Healer
- Phone Number : +94712583690
- website : www.lumenglowstudio.example
- email : lumengrovestudio@mailbox.example

Services offered :
REIKI ENERGY HEALING
DISTANCE HEALING
STRESS MANAGEMENT
PRANAYAMA
KUNDALINI
ART THERAPY
DANCE THERAPY
COUNSELLING
TAI CHI

IMPORTANT : Designers should refrain from posting designs done in any online mediums in their portfolio other than in freelancer to avoid others copying brand name and design ideas

```html
<!DOCTYPE html>
<html lang="en">
<head>
<meta charset="utf-8">
<title>Lumen Grove – Business Card</title>
<link rel="stylesheet" href="https://fonts.googleapis.com/css2?family=Montserrat:wght@400;500;600;700&display=swap">
<style>
  :root {
    --purple: #8a5cb8;
    --purple-deep: #6f4299;
    --white: #ffffff;
    --paper: #fbfafd;
    --backdrop: #ece8f1;
    --ink-muted: #7d6a92;
  }
  * { box-sizing: border-box; margin: 0; padding: 0; }
  html, body { width: 1200px; height: 891px; overflow: hidden; }
  body {
    background: var(--backdrop);
    font-family: "Montserrat", Arial, sans-serif;
    position: relative;
  }
  .card {
    position: absolute;
    left: 280px;
    width: 640px;
    height: 366px;
    border-radius: 6px;
    box-shadow: 0 8px 24px rgba(60, 30, 90, 0.18);
    overflow: hidden;
  }

  /* ---------- Brand name (plain text, one colour, one weight) ---------- */
  .brand {
    position: absolute;
    display: flex;
    flex-direction: column;
    align-items: center;
  }
  .brand-mark {
    width: 50px; height: 50px;
    border-radius: 50%;
    border: 2px solid currentColor;
    margin-bottom: 16px;
  }
  .brand-name {
    font-weight: 600;
    font-size: 26px;
    letter-spacing: 0;
    white-space: nowrap;
  }

  /* ---------- Back: services ---------- */
  .card--services {
    top: 50px;
    background: var(--purple);
    color: var(--white);
  }
  .card--services .inner-frame {
    position: absolute;
    inset: 12px;
    border: 1.5px solid rgba(255,255,255,0.85);
  }
  .card--services .brand { left: 40px; top: 118px; width: 270px; }
  .card--services .divider {
    position: absolute;
    left: 338px; top: 52px;
    width: 2px; height: 262px;
    background: var(--white);
  }
  .services {
    position: absolute;
    left: 360px; top: 56px;
  }
  .services-title {
    font-weight: 600;
    font-size: 17px;
    margin-bottom: 12px;
  }
  .services-list {
    list-style: none;
    font-weight: 600;
    font-size: 14px;
    line-height: 24px;
    letter-spacing: 0.3px;
  }
  .services-list li::before { content: "."; }

  /* ---------- Front: contact ---------- */
  .card--contact {
    top: 475px;
    background: var(--paper);
    color: var(--purple-deep);
  }
  .card--contact .brand { left: 30px; top: 62px; width: 270px; color: var(--purple); }
  .card--contact .brand-name { font-size: 24px; }
  .card--contact .divider {
    position: absolute;
    left: 316px; top: 56px;
    width: 2px; height: 200px;
    background: var(--purple);
  }
  .person {
    position: absolute;
    left: 338px; top: 66px;
  }
  .person-name {
    font-weight: 700;
    font-size: 21px;
    color: var(--purple);
  }
  .person-role {
    font-size: 11px;
    color: var(--ink-muted);
    margin-top: 3px;
  }
  .contact-list {
    list-style: none;
    margin-top: 22px;
    font-size: 13px;
    color: var(--purple-deep);
  }
  .contact-list li {
    display: flex;
    align-items: center;
    gap: 10px;
    height: 26px;
  }
  .contact-list svg { width: 14px; height: 14px; flex: none; fill: var(--purple); }
  .address-band {
    position: absolute;
    left: 0; right: 0; bottom: 0;
    height: 44px;
    background: var(--purple);
    color: var(--white);
    display: flex;
    align-items: center;
    gap: 12px;
    padding-left: 24px;
    font-size: 14px;
    font-weight: 500;
  }
  .address-band svg { width: 16px; height: 16px; fill: var(--white); flex: none; }
</style>
</head>
<body>

  <section class="card card--services" aria-label="Business card back">
    <div class="inner-frame"></div>
    <div class="brand">
      <span class="brand-mark"></span>
      <span class="brand-name">LUMEN GROVE</span>
    </div>
    <div class="divider"></div>
    <div class="services">
      <h2 class="services-title">Services offered :</h2>
      <ul class="services-list">
        <li>REIKI ENERGY HEALING</li>
        <li>DISTANCE HEALING</li>
        <li>STRESS MANAGEMENT</li>
        <li>PRANAYAMA</li>
        <li>KUNDALINI</li>
        <li>ART THERAPY</li>
        <li>DANCE THERAPY</li>
        <li>COUNSELLING</li>
        <li>TAI CHI</li>
      </ul>
    </div>
  </section>

  <section class="card card--contact" aria-label="Business card front">
    <div class="brand">
      <span class="brand-mark"></span>
      <span class="brand-name">LUMEN GROVE</span>
    </div>
    <div class="divider"></div>
    <div class="person">
      <h1 class="person-name">Mala Wickramaratne</h1>
      <p class="person-role">Founder / Reiki Healer</p>
      <ul class="contact-list">
        <li>
          <svg viewBox="0 0 24 24" aria-hidden="true"><path d="M6.6 10.8a15.1 15.1 0 0 0 6.6 6.6l2.2-2.2a1 1 0 0 1 1-.25 11.4 11.4 0 0 0 3.6.57 1 1 0 0 1 1 1V20a1 1 0 0 1-1 1A17 17 0 0 1 3 4a1 1 0 0 1 1-1h3.5a1 1 0 0 1 1 1c0 1.25.2 2.45.57 3.57a1 1 0 0 1-.25 1z"/></svg>
          +94712583690
        </li>
        <li>
          <svg viewBox="0 0 24 24" aria-hidden="true"><path d="M3 5h18a1 1 0 0 1 1 1v12a1 1 0 0 1-1 1H3a1 1 0 0 1-1-1V6a1 1 0 0 1 1-1zm9 7.5L4 7.3V17h16V7.3z"/></svg>
          lumengrovestudio@mailbox.example
        </li>
        <li>
          <svg viewBox="0 0 24 24" aria-hidden="true"><path d="M12 2a10 10 0 1 0 0 20 10 10 0 0 0 0-20zm6.9 6h-3a15.6 15.6 0 0 0-1.3-3.6A8 8 0 0 1 18.9 8zM12 4c.8 1.2 1.5 2.5 1.9 4h-3.8c.4-1.5 1.1-2.8 1.9-4zM4.3 14a8 8 0 0 1 0-4h3.4a16 16 0 0 0 0 4zm.8 2h3a15.6 15.6 0 0 0 1.3 3.6A8 8 0 0 1 5.1 16zm3-8h-3a8 8 0 0 1 4.3-3.6A15.6 15.6 0 0 0 8.1 8zM12 20c-.8-1.2-1.5-2.5-1.9-4h3.8c-.4 1.5-1.1 2.8-1.9 4zm2.3-6H9.7a14.7 14.7 0 0 1 0-4h4.6a14.7 14.7 0 0 1 0 4zm.3 5.6a15.6 15.6 0 0 0 1.3-3.6h3a8 8 0 0 1-4.3 3.6zm1.7-5.6a16 16 0 0 0 0-4h3.4a8 8 0 0 1 0 4z"/></svg>
          www.lumenglowstudio.example
        </li>
      </ul>
    </div>
    <div class="address-band">
      <svg viewBox="0 0 24 24" aria-hidden="true"><path d="M12 2a7 7 0 0 0-7 7c0 5.2 7 13 7 13s7-7.8 7-13a7 7 0 0 0-7-7zm0 9.5A2.5 2.5 0 1 1 12 6.5a2.5 2.5 0 0 1 0 5z"/></svg>
      No 8, Perera Crescent, Galvin Lane, Colombo 5, Sri Lanka
    </div>
  </section>

</body>
</html>
```